<作成物>
■リッチメッセージ
リッチメニュー
合計2枚
リッチメニュー の表示項目は画像写真添付します。
写真添付しております。

【デザインの詳細】
オレンジ(画像の女性のエプロンのオレンジと似せてください)
をベースに元気でハッピーになれるような感じを希望しております。
使用される画像は添付のアドレスに入ってりますの
でどれを使用されても構いません。
イメージのデザイン合わせた感じにしていただけると嬉しいです。
https://files.tovrelink-share.example/dl/5k2m9q7x3c8v1b4n6z0p
上下で一体感があるものを希望します。
人物の画像は入れても入れなくても(デザインで決めてください)

【表示文言】
上の画像に入れる文言
工作感覚で作るから初めてでも大丈夫!
可愛い過ぎるお寿司レッスン
(文字がデザイン的に合わなければ入れなくてもOK)

〈リッチメニューの表示項目〉
画像の中に入れますの、これを参考に入れてください。

デザイン重視でここの表示名はデザイン的に英語の方がよければ
英語でも大丈夫です。意味がわかって
ニュアンスがあっていれば文字を短くするのも
お任せします。あくまでデザイン重視です。
〈画像はこちらから〉
画像

※こちらの作成以外に勝手に使用された場合は
著作権侵害で法的手段をとらせていただきます。
作成事例にもしようしないでください。

<サイズ>
・リッチメッセージ(1040×1040ピクセル)
・リッチメニュー(1200×810ピクセル)

<納品形式>
・ai形式(イラストレーターデータ)
・JPG
<詳細>
※添付ファイルをご確認ください。

<備考>
ブランディング効果を期待しています。
どんどん何個でも応募ください。

```html
<!DOCTYPE html>
<html lang="ja">
<head>
<meta charset="utf-8">
<title>お寿司レッスン リッチメッセージ・リッチメニュー</title>
<link rel="stylesheet" href="https://fonts.googleapis.com/css2?family=Zen+Maru+Gothic:wght@500;700;900&family=Playball&display=swap">
<style>
  :root {
    --page: #ffffff;
    --orange: #ef8a17;
    --orange-deep: #d96f0c;
    --sun: #f8bf33;
    --sun-soft: rgba(248, 196, 60, 0.9);
    --ink: #2f2a22;
    --white: #ffffff;
    --photo-a: #e9b9b6;
    --photo-b: #c9a37a;
    --photo-c: #8f6f7a;
    --photo-d: #e8d3c0;
  }
  * { box-sizing: border-box; margin: 0; padding: 0; }
  html, body { width: 798px; height: 1200px; overflow: hidden; background: var(--page); }
  body { position: relative; font-family: "Zen Maru Gothic", sans-serif; color: var(--ink); }

  /* Rich message */
  .message {
    position: absolute; left: 93px; top: 40px; width: 612px; height: 612px; overflow: hidden;
  }
  .message__photo {
    position: absolute; inset: 0;
    background:
      radial-gradient(circle at 20% 20%, var(--photo-d) 0 18%, transparent 40%),
      radial-gradient(circle at 82% 22%, var(--photo-c) 0 12%, transparent 34%),
      radial-gradient(circle at 22% 82%, var(--photo-a) 0 14%, transparent 36%),
      radial-gradient(circle at 80% 80%, var(--photo-c) 0 16%, transparent 38%),
      linear-gradient(135deg, var(--photo-a), var(--photo-b) 55%, var(--photo-d));
  }
  .message__badge {
    position: absolute; left: 131px; top: 108px; width: 350px; height: 350px; border-radius: 50%;
    background: var(--sun-soft);
  }
  .message__lead {
    position: absolute; left: 0; right: 0; top: 62px; text-align: center;
    color: var(--orange-deep); font-weight: 900; font-size: 26px; white-space: nowrap;
    transform: rotate(-5deg);
  }
  .message__sub {
    position: absolute; left: 0; right: 0; top: 132px; text-align: center;
    color: var(--white); font-weight: 700; font-size: 28px; white-space: nowrap;
  }
  .message__title {
    position: absolute; left: -30px; right: -30px; top: 180px; text-align: center;
    color: var(--white); font-weight: 900; font-size: 42px; line-height: 1.3; letter-spacing: 1px;
    white-space: nowrap; padding-bottom: 6px; border-bottom: 5px solid var(--orange);
  }
  .message__title-accent { color: var(--orange-deep); }

  /* Rich menu */
  .menu {
    position: absolute; left: 40px; top: 697px; width: 718px; height: 478px; overflow: hidden;
  }
  .menu__photo {
    position: absolute; inset: 0;
    background:
      radial-gradient(circle at 30% 30%, var(--photo-d) 0 15%, transparent 40%),
      radial-gradient(circle at 75% 70%, var(--photo-a) 0 15%, transparent 40%),
      linear-gradient(160deg, var(--photo-d), var(--photo-a) 50%, var(--photo-b));
  }
  .menu__grid {
    position: absolute; inset: 10px; display: grid;
    grid-template-columns: repeat(3, 1fr); grid-template-rows: repeat(2, 1fr); gap: 10px;
  }
  .tile {
    position: relative; background: var(--sun-soft); border: 3px solid var(--ink);
  }
  .tile__label {
    position: absolute; left: 0; right: 0; top: 12px; text-align: center;
    font-family: "Playball", cursive; font-size: 30px; line-height: 1; color: var(--ink);
  }
  .tile__icon { position: absolute; left: 50%; top: 56px; width: 96px; height: 96px; margin-left: -48px; }
  .tile__caption {
    position: absolute; left: 0; right: 0; top: 160px; text-align: center;
    font-size: 20px; font-weight: 700; white-space: nowrap;
  }
</style>
</head>
<body>
  <section class="message">
    <div class="message__photo" role="img" aria-label="色とりどりの飾り巻き寿司と花形寿司の写真コラージュ"></div>
    <div class="message__badge">
      <p class="message__lead">初めてでも大丈夫!</p>
      <p class="message__sub">可愛い過ぎる</p>
      <h1 class="message__title">お<span class="message__title-accent">寿司</span>レッスン</h1>
    </div>
  </section>

  <section class="menu">
    <div class="menu__photo" role="img" aria-label="花模様の飾り巻き寿司の断面写真"></div>
    <div class="menu__grid">
      <div class="tile">
        <span class="tile__label">Menu</span>
        <svg class="tile__icon" viewBox="0 0 96 96" fill="none" stroke="var(--ink)" stroke-width="4">
          <rect x="22" y="12" width="52" height="72" rx="3"/>
          <line x1="30" y1="30" x2="66" y2="30"/><line x1="30" y1="44" x2="66" y2="44"/>
          <line x1="30" y1="56" x2="66" y2="56"/><line x1="30" y1="68" x2="56" y2="68"/>
        </svg>
        <span class="tile__caption">お寿司</span>
      </div>
      <div class="tile">
        <span class="tile__label">Suhedule</span>
        <svg class="tile__icon" viewBox="0 0 96 96" fill="none" stroke="var(--ink)" stroke-width="4">
          <rect x="16" y="20" width="64" height="60" rx="4"/>
          <line x1="16" y1="36" x2="80" y2="36"/>
          <line x1="32" y1="12" x2="32" y2="26"/><line x1="64" y1="12" x2="64" y2="26"/>
          <g fill="var(--ink)" stroke="none">
            <rect x="26" y="46" width="8" height="8"/><rect x="44" y="46" width="8" height="8"/><rect x="62" y="46" width="8" height="8"/>
            <rect x="26" y="62" width="8" height="8"/><rect x="44" y="62" width="8" height="8"/>
          </g>
        </svg>
        <span class="tile__caption">空席状況</span>
      </div>
      <div class="tile">
        <span class="tile__label">Event</span>
        <svg class="tile__icon" viewBox="0 0 96 96" fill="var(--ink)">
          <rect x="45" y="50" width="6" height="38"/>
          <path d="M48 54 C30 54 12 42 10 22 C32 22 46 34 48 54 Z"/>
          <path d="M48 54 C66 54 84 42 86 22 C64 22 50 34 48 54 Z"/>
        </svg>
      </div>
      <div class="tile">
        <span class="tile__label">HP</span>
        <svg class="tile__icon" viewBox="0 0 96 96" fill="none" stroke="var(--ink)" stroke-width="4">
          <rect x="12" y="18" width="72" height="48" rx="3"/>
          <line x1="48" y1="66" x2="48" y2="78"/><line x1="32" y1="80" x2="64" y2="80"/>
          <path d="M38 36 L58 42 L48 46 L44 56 Z" fill="var(--ink)"/>
        </svg>
      </div>
      <div class="tile">
        <span class="tile__label">SNS</span>
        <svg class="tile__icon" viewBox="0 0 96 96" fill="none" stroke="var(--ink)" stroke-width="4">
          <circle cx="48" cy="48" r="30"/>
          <ellipse cx="48" cy="48" rx="13" ry="30"/>
          <line x1="18" y1="48" x2="78" y2="48"/>
          <line x1="22" y1="34" x2="74" y2="34"/><line x1="22" y1="62" x2="74" y2="62"/>
        </svg>
      </div>
      <div class="tile">
        <span class="tile__label">Lesson</span>
        <svg class="tile__icon" viewBox="0 0 96 96" fill="var(--ink)">
          <path d="M36 10 L60 10 L60 30 L74 22 L78 28 L64 40 L70 88 L26 88 L32 40 L18 28 L22 22 L36 30 Z"/>
          <rect x="40" y="58" width="16" height="12" fill="var(--sun)"/>
        </svg>
        <span class="tile__caption">対面・ONLINE</span>
      </div>
    </div>
  </section>
</body>
</html>
```